Business card for exciting VC company

Should look simple, crisp, and modern.

Industry/Entity Type

Venture Capital

Contact Information for Business Card

Would like to see at least one design that has our blue on the back with the tagline "Transforming Traditional Industry" and white front with contact details.

Font styles to use
Sans Serif

Requirements
Must have
• Logo

Gregory Tallis
gtallis@brindlewave.vc
Managing Partner
M (628)354-xxxx

```html
<!DOCTYPE html>
<html lang="en">
<head>
<meta charset="utf-8">
<title>Brindlewave Capital – Business Card</title>
<link href="https://fonts.googleapis.com/css2?family=Lato:wght@400;700&display=swap" rel="stylesheet">
<style>
  :root {
    --brand-blue: #4383c5;
    --ink: #050708;
    --paper: #ffffff;
    --stage: #2a2a2a;
  }
  * { box-sizing: border-box; margin: 0; padding: 0; }
  html, body {
    width: 1200px; height: 900px; overflow: hidden;
    background: var(--stage);
    font-family: "Lato", sans-serif;
  }
  .sheet {
    position: relative; width: 1200px; height: 900px;
    display: flex; flex-direction: column; align-items: center; justify-content: center; gap: 24px;
  }
  .card {
    position: relative; width: 700px; height: 400px; overflow: hidden;
  }

  /* Back */
  .card-back { background: var(--brand-blue); }
  .card-back .wordmark {
    position: absolute; top: 130px; left: 0; right: 0; text-align: center; color: var(--ink);
  }
  .wordmark-name {
    display: block; font-weight: 700; font-size: 56px; letter-spacing: 6px; line-height: 1;
  }
  .wordmark-sub {
    display: block; font-weight: 700; font-size: 18px; letter-spacing: 10px; margin-top: 10px;
  }
  .tagline {
    position: absolute; bottom: 46px; left: 0; right: 0; text-align: center;
    color: var(--paper); font-weight: 700; font-size: 17px; letter-spacing: 1.5px; text-transform: uppercase;
  }

  /* Front */
  .card-front { background: var(--ink); }
  .card-front .swoosh { position: absolute; inset: 0; }
  .card-front .wordmark {
    position: absolute; top: 58px; left: 40px; color: var(--ink);
  }
  .card-front .wordmark-name { font-size: 42px; letter-spacing: 4px; }
  .card-front .wordmark-sub { font-size: 15px; letter-spacing: 8px; margin-top: 8px; padding-left: 100px; }

  .contact {
    position: absolute; right: 44px; bottom: 40px; text-align: right; color: var(--paper);
  }
  .contact-name {
    color: var(--brand-blue); font-weight: 700; font-size: 22px; letter-spacing: 1px; text-transform: uppercase;
  }
  .contact-title { font-size: 20px; margin-top: 2px; }
  .contact-lines { margin-top: 30px; font-size: 20px; line-height: 1.45; }
  .contact-line { display: flex; align-items: center; justify-content: flex-end; gap: 12px; }
  .contact-line svg { width: 20px; height: 20px; flex: none; }
</style>
</head>
<body>
<main class="sheet">

  <section class="card card-back" aria-label="Card back">
    <div class="wordmark">
      <span class="wordmark-name">BRINDLEWAVE</span>
      <span class="wordmark-sub">CAPITAL</span>
    </div>
    <p class="tagline">Transforming Traditional Industry</p>
  </section>

  <section class="card card-front" aria-label="Card front">
    <svg class="swoosh" viewBox="0 0 700 400" width="700" height="400" aria-hidden="true">
      <path d="M0,0 H660 C520,120 300,250 110,262 C60,265 25,262 0,255 Z" fill="var(--brand-blue)"/>
      <path d="M0,248 C25,255 60,258 110,255 C300,243 515,115 650,0" fill="none" stroke="var(--paper)" stroke-width="3"/>
      <path d="M0,0 H635 C495,105 330,205 200,218 C100,228 25,200 0,170 Z" fill="var(--paper)"/>
    </svg>
    <div class="wordmark">
      <span class="wordmark-name">BRINDLEWAVE</span>
      <span class="wordmark-sub">CAPITAL</span>
    </div>
    <div class="contact">
      <p class="contact-name">Gregory Tallis</p>
      <p class="contact-title">Managing Partner</p>
      <div class="contact-lines">
        <p class="contact-line">(628)354-xxxx
          <svg viewBox="0 0 24 24" aria-hidden="true"><circle cx="12" cy="12" r="10" fill="none" stroke="var(--brand-blue)" stroke-width="1.6"/><path d="M8.5 7.5c.5-.6 1.3-.6 1.7 0l1 1.4c.3.5.2 1.1-.2 1.4l-.6.5c.6 1.3 1.6 2.3 2.9 2.9l.5-.6c.4-.4 1-.5 1.4-.2l1.4 1c.6.4.6 1.2 0 1.7-1 .9-2.4 1.1-3.6.4-2.300-1.2-4.1-3-5.3-5.3-.6-1.2-.4-2.6.5-3.6z" fill="var(--brand-blue)"/></svg>
        </p>
        <p class="contact-line">gtallis@brindlewave.vc
          <svg viewBox="0 0 24 24" aria-hidden="true"><rect x="2" y="5" width="20" height="14" rx="1.5" fill="none" stroke="var(--brand-blue)" stroke-width="1.6"/><path d="M2.5 6l9.5 7.5L21.5 6M2.5 18.5l7-6M21.5 18.5l-7-6" fill="none" stroke="var(--brand-blue)" stroke-width="1.6"/></svg>
        </p>
      </div>
    </div>
  </section>

</main>
</body>
</html>
```